Accounting and Financial Services Firm - Modern, Fresh, Original, Professional

We need a business card designed. We would like to see use of the the colors blue. Logo attached.

Modern, Fresh, Original, Professional,
Updates

Email section on business card required. design brief updated.

Target Market(s)

Small to medium businesses and high net worth individuals

Industry/Entity Type

Public Accounting

Contact Information for Business Card

Business Name: PM Ledgerline Chartered Accountants
Address: Level 14, 82 Harrow Lane Sydney NSW 2000
Ph: 02 9314 2587
Mobile: 04 XXXX XXXX
Email: anna@pmledgerline.com.au
Wechat ID: XXXXXXX
Website: www.pmledgerline.com.au

Name: Anna Petrov
Position: Manager

Font styles to use
Sans Serif

Colors
0492cd
33a6d7
85cae6

Requirements
Must have
• Modern font.

```html
<!DOCTYPE html>
<html lang="en">
<head>
<meta charset="utf-8">
<title>PM Ledgerline – Business Card</title>
<link rel="stylesheet" href="https://fonts.googleapis.com/css2?family=Montserrat:wght@400;500&family=Ubuntu:wght@400;500&display=swap">
<style>
  :root {
    --blue: #0492cd;
    --blue-mid: #33a6d7;
    --blue-light: #85cae6;
    --tint: #e4f1f8;
    --grey-tint: #eef0f2;
    --ink: #3a3f45;
    --paper: #ffffff;
    --stage: #ecedee;
  }
  * { box-sizing: border-box; margin: 0; padding: 0; }
  html, body { width: 1200px; height: 1200px; overflow: hidden; }
  body {
    background: var(--stage);
    font-family: "Ubuntu", sans-serif;
    display: flex;
    flex-direction: column;
    align-items: center;
    justify-content: center;
    gap: 52px;
  }
  .card {
    position: relative;
    width: 900px;
    height: 514px;
    background: var(--paper);
    overflow: hidden;
    box-shadow: 0 6px 18px rgba(0,0,0,.12);
  }
  .pattern {
    position: absolute;
    inset: 0;
    background:
      linear-gradient(160deg, var(--tint) 0%, var(--paper) 38%, var(--grey-tint) 62%, var(--tint) 100%);
  }
  .brand {
    position: absolute;
    display: flex;
    align-items: center;
    gap: 16px;
    color: var(--blue);
    font-family: "Montserrat", sans-serif;
    font-weight: 400;
    white-space: nowrap;
  }
  .brand-mark {
    width: 22px; height: 22px;
    background: var(--blue);
    flex: none;
  }
  .brand-name { font-size: 46px; letter-spacing: 2px; line-height: 1; text-transform: uppercase; }
  .brand-sub { font-size: 14px; letter-spacing: 4px; margin-top: 8px; text-transform: uppercase; }

  /* front */
  .card-front .brand { left: 50%; top: 50%; transform: translate(-50%, -50%); }

  /* back */
  .card-back .pattern {
    right: auto;
    width: 47%;
  }
  .card-back .brand { left: 56px; top: 200px; }
  .card-back .brand-name { font-size: 34px; letter-spacing: 1px; }
  .card-back .brand-sub { font-size: 11px; letter-spacing: 3px; }
  .person {
    position: absolute;
    left: 470px;
    top: 140px;
    font-family: "Montserrat", sans-serif;
  }
  .person-name { color: var(--blue); font-size: 34px; font-weight: 400; text-transform: uppercase; letter-spacing: .5px; white-space: nowrap; }
  .person-role { color: var(--ink); font-size: 17px; margin-top: 6px; font-family: "Ubuntu", sans-serif; }
  .contacts {
    position: absolute;
    left: 470px;
    top: 240px;
    width: 400px;
    color: var(--ink);
    font-size: 16px;
  }
  .contact-cols { display: flex; border-top: 1px solid var(--blue-light); padding-top: 14px; }
  .contact-col { display: flex; flex-direction: column; gap: 10px; }
  .contact-col:first-child { width: 150px; flex: none; }
  .contact-col + .contact-col { flex: 1; border-left: 1px solid var(--blue-light); padding-left: 14px; }
  .contact-row { display: flex; align-items: center; gap: 10px; white-space: nowrap; }
  .icon { width: 16px; height: 16px; flex: none; fill: var(--blue); }
  .address { border-top: 1px solid var(--blue-light); margin-top: 14px; padding-top: 14px; }
  .band {
    position: absolute;
    left: 47%;
    right: 0;
    bottom: 0;
    height: 62px;
    background: var(--blue);
  }
</style>
</head>
<body>

<section class="card card-front">
  <div class="pattern" role="img" aria-label="Soft geometric pattern of pale blue and grey translucent panels"></div>
  <div class="brand">
    <span class="brand-mark"></span>
    <div>
      <div class="brand-name">PM Ledgerline</div>
      <div class="brand-sub">Chartered Accountants</div>
    </div>
  </div>
</section>

<section class="card card-back">
  <div class="pattern" role="img" aria-label="Soft geometric pattern of pale blue and grey translucent panels"></div>
  <div class="brand">
    <span class="brand-mark"></span>
    <div>
      <div class="brand-name">PM Ledgerline</div>
      <div class="brand-sub">Chartered Accountants</div>
    </div>
  </div>

  <div class="person">
    <div class="person-name">Anna Petrov</div>
    <div class="person-role">Manager</div>
  </div>

  <div class="contacts">
    <div class="contact-cols">
      <div class="contact-col">
        <div class="contact-row">
          <svg class="icon" viewBox="0 0 16 16"><circle cx="8" cy="8" r="7"/></svg>
          <span>XXXXXXX</span>
        </div>
        <div class="contact-row">
          <svg class="icon" viewBox="0 0 16 16"><path d="M4 0h8a1 1 0 0 1 1 1v14a1 1 0 0 1-1 1H4a1 1 0 0 1-1-1V1a1 1 0 0 1 1-1zm1 2v9h6V2zm3 10.5a1 1 0 1 0 0 2 1 1 0 0 0 0-2z"/></svg>
          <span>04 XXXX XXXX</span>
        </div>
      </div>
      <div class="contact-col">
        <div class="contact-row">
          <svg class="icon" viewBox="0 0 16 16"><path d="M1 5c0-2 3-3 7-3s7 1 7 3v2h-3V5.5H4V7H1zm2 3h10l1 6H2z"/></svg>
          <span>02 9314 2587</span>
        </div>
        <div class="contact-row">
          <svg class="icon" viewBox="0 0 16 16"><path d="M1 3h14v10H1zm1.5 1.5v.3L8 8.6l5.5-3.8v-.3zm0 2.1v4.9h11V6.6L8 10.4z"/></svg>
          <span>anna@pmledgerline.com.au</span>
        </div>
        <div class="contact-row">
          <svg class="icon" viewBox="0 0 16 16"><path d="M8 0a8 8 0 1 0 0 16A8 8 0 0 0 8 0zm0 1.5c.8 0 1.9 1.7 2.3 4.5H5.7C6.1 3.2 7.2 1.5 8 1.5zM1.6 7h3.9a14 14 0 0 0 0 2H1.6a6.5 6.5 0 0 1 0-2zm5 0h2.8a13 13 0 0 1 0 2H6.6a13 13 0 0 1 0-2zm3.9 0h3.9a6.5 6.5 0 0 1 0 2h-3.9a14 14 0 0 0 0-2zM5.7 10h4.6c-.4 2.8-1.5 4.5-2.3 4.5S6.1 12.8 5.7 10z"/></svg>
          <span>www.pmledgerline.com.au</span>
        </div>
      </div>
    </div>
    <div class="contact-row address">
      <svg class="icon" viewBox="0 0 16 16"><path d="M8 0a5.5 5.5 0 0 0-5.5 5.5C2.5 10 8 16 8 16s5.5-6 5.5-10.5A5.5 5.5 0 0 0 8 0zm0 3a2.5 2.5 0 1 1 0 5 2.5 2.5 0 0 1 0-5z"/></svg>
      <span>Level 14, 82 Harrow Lane, Sydney NSW 2000</span>
    </div>
  </div>

  <div class="band"></div>
</section>

</body>
</html>
```